Sena & Kaan Wedding Invitation and Decorative Designs

We are looking for a sweet and elegant design for our wedding invitation. We need different versions of the same design to use both as printed hard copies and in digital formats (WhatsApp image, instagram post, etc) Please see attached sample invitation, which we like as a simple and elegant option, but also find it quite basic. We are open to creative suggestions following a similar style.
Once we decide on an invitation design, we would like to use the same design elements in guest name cards, welcome sign, menu cards and print cover for the dance floor of our wedding venue. Please see random samples of these materials attached. We also attach a photo from our wedding venue displaying a close to final visual of the decoration we chose for our wedding day (sharing in case it helps as an inspiration source and helps with matching decoration colors with the designs)
- Must have a style similar to the attached sample invitation

```html
<!DOCTYPE html>
<html lang="en">
<head>
<meta charset="utf-8">
<title>Sena &amp; Kaan — Wedding Invitation</title>
<link href="https://fonts.googleapis.com/css2?family=Tulpen+One&display=swap" rel="stylesheet">
<style>
  :root{
    --paper:#ffffff;
    --peach:#fef3e8;
    --diamond:#f8f6f7;
    --lilac:#a992bd;
    --lilac-soft:#e7e3ef;
    --leaf-light:#fbf8fc;
    --leaf-mid:#e4d6e6;
    --leaf-deep:#ab8aa2;
    --shadow:#d6d6d6;
  }
  *{margin:0;padding:0;box-sizing:border-box;}
  html,body{width:1200px;height:1200px;overflow:hidden;background:var(--paper);}
  .invitation{position:relative;width:1200px;height:1200px;overflow:hidden;background:var(--paper);
    font-family:"Tulpen One",sans-serif;color:var(--lilac);}
  .backdrop{position:absolute;inset:0;}
  .label,.names,.date{position:absolute;line-height:1;white-space:nowrap;}
  .label{left:52px;top:44px;font-size:118px;letter-spacing:26px;}
  .names{left:404px;top:442px;font-size:196px;letter-spacing:22px;}
  .names span{display:block;height:178px;}
  .date-month{left:721px;top:1120px;font-size:78px;letter-spacing:12px;}
  .date-day{left:890px;top:1062px;font-size:152px;letter-spacing:10px;}
  .year-box{position:absolute;left:1000px;top:1073px;width:200px;height:127px;background:var(--lilac-soft);}
  .date-year{left:1028px;top:1090px;font-size:126px;letter-spacing:10px;}
  .foliage{position:absolute;}
</style>
</head>
<body>
<main class="invitation">
  <svg class="backdrop" width="1200" height="1200" viewBox="0 0 1200 1200" aria-hidden="true">
    <defs>
      <radialGradient id="plateShadow" cx="0.5" cy="0.5" r="0.5">
        <stop offset="0.85" stop-color="#cfcfcf"/>
        <stop offset="1" stop-color="#e6e6e6"/>
      </radialGradient>
    </defs>
    <rect class="peach-block" x="0" y="0" width="609" height="614" fill="var(--peach)"/>
    <polygon class="diamond" points="609,59 1163,614 609,1169 56,614" fill="var(--diamond)"/>
    <circle class="plate-shadow" cx="634" cy="645" r="332" fill="url(#plateShadow)"/>
    <circle class="plate" cx="605" cy="615" r="332" fill="var(--paper)" stroke="#bdbdbd" stroke-width="0.6"/>
  </svg>

  <svg class="foliage foliage-left" role="img" aria-label="Paper-cut leafy branch with white and mauve leaves curving along the left side"
       style="left:28px;top:228px" width="480" height="860" viewBox="0 0 480 860">
    <defs>
      <linearGradient id="leafLeft" x1="0" y1="0" x2="1" y2="1">
        <stop offset="0" stop-color="var(--leaf-mid)"/>
        <stop offset="0.35" stop-color="var(--leaf-light)"/>
        <stop offset="1" stop-color="var(--leaf-mid)"/>
      </linearGradient>
    </defs>
    <path d="M250,10 C330,80 360,160 320,230 C250,300 210,380 200,470 C230,560 330,640 470,830 C380,860 250,830 170,760 C60,660 0,520 10,400 C20,240 120,90 250,10 Z" fill="url(#leafLeft)"/>
  </svg>

  <svg class="foliage foliage-right" role="img" aria-label="Paper-cut leafy branch with white and mauve leaves rising on the right side"
       style="left:732px;top:644px" width="420" height="420" viewBox="0 0 420 420">
    <defs>
      <linearGradient id="leafRight" x1="1" y1="0" x2="0" y2="1">
        <stop offset="0" stop-color="var(--leaf-mid)"/>
        <stop offset="0.4" stop-color="var(--leaf-light)"/>
        <stop offset="1" stop-color="var(--leaf-mid)"/>
      </linearGradient>
    </defs>
    <path d="M380,0 C420,60 420,160 380,240 C330,330 220,380 120,390 C70,400 20,410 0,420 C60,330 120,250 150,180 C200,90 290,30 380,0 Z" fill="url(#leafRight)"/>
  </svg>

  <h2 class="label">INVITATION</h2>

  <h1 class="names"><span>SENA</span><span>&amp; KAAN</span></h1>

  <div class="year-box"></div>
  <p class="date date-month">APRIL</p>
  <p class="date date-day">30</p>
  <p class="date date-year">2024</p>
</main>
</body>
</html>
```